High Tech Health: Telehealth Tablets

mirabelQuorix is an innovative telehealth company based in Los Angeles, and we need a postcard design. We help patients to navigate our broken healthcare system. We provide tablet PC's to healthcare patients to keep in their homes, and it allows us to have video chats with our patients so they can have face to face discussions and feel more connected as they battle their illness.

We have a general idea of what the design might look like.

Front side: the front must look as if the postcard is a tablet PC (see first attached image for an idea). Specifically, the edges of the front side will be black for around 1 inch or so, just as if it is an Zolvo. Inside the black tablet border should be something about either video conferencing technology through the tablet (see second attached image 'videochat' of a patient and a caring professional), or improved patient quality of life.

Rear side: the back side might have an infographic (see third attached 'nodes' photo), a middle section with written words, and the right side can have the mobile devices pictures (smartphone, tablet, pc). We are open and flexible to your creativity.

Overall design: we want to give the feeling of a high tech solution that keeps patient secure. We attached a very rough sketch of what the front and back might look like.

Thank you very much to all of you for your hard work on this project. We are communicating with one designer towards finalizing the project, so unless something changes, we have what we need for this postcard. Thanks again! We will be posting more projects in the future and look forward to working with everyone.

```html
<!DOCTYPE html>
<html lang="en">
<head>
<meta charset="utf-8">
<title>Veltrona CareLoom Postcard</title>
<link rel="stylesheet" href="https://fonts.googleapis.com/css2?family=Source+Sans+3:wght@400;600;700&display=swap">
<style>
  :root {
    --page: #e9e6e1;
    --card: #ffffff;
    --navy: #1d4a8f;
    --navy-deep: #12306b;
    --rule: #4f8fd0;
    --band: #1f6fc4;
    --green: #2f6a2e;
    --green-edge: #ffffff;
    --text: #3a3a3a;
    --bezel: #1e1c1d;
    --bezel-edge: #3a3839;
    --pill: #5b5e63;
  }
  * { box-sizing: border-box; margin: 0; padding: 0; }
  html, body { width: 1200px; height: 1000px; overflow: hidden; }
  body {
    background: var(--page);
    font-family: "Source Sans 3", "Myriad Pro", sans-serif;
    position: relative;
  }

  /* ---------- back side ---------- */
  .postcard-back {
    position: absolute; left: 250px; top: 40px;
    width: 700px; height: 440px;
    background: var(--card);
    box-shadow: 0 4px 14px rgba(0,0,0,.18);
  }
  .node-map { position: absolute; left: 10px; top: 100px; width: 200px; height: 240px; }
  .node-map text { font-family: "Source Sans 3", sans-serif; font-weight: 700; fill: #fff; }
  .column-rule { position: absolute; top: 36px; width: 2px; height: 370px; background: var(--rule); }
  .column-rule.left { left: 215px; }
  .column-rule.right { left: 482px; }

  .copy-column {
    position: absolute; left: 230px; top: 40px; width: 244px; height: 376px;
    display: flex; flex-direction: column;
  }
  .section-title {
    color: var(--navy); font-weight: 700; font-size: 13px; line-height: 1.2;
  }
  .section-title span { display: block; white-space: nowrap; }
  .intro-text {
    margin-top: 22px; color: var(--text); font-size: 10.5px; line-height: 1.35;
  }
  .feature-title { margin-top: 34px; }
  .feature-list { margin-top: 14px; list-style: none; color: var(--text); font-size: 11px; line-height: 1.3; }
  .copy-column .wordmark {
    margin-top: auto; padding-left: 60px;
    color: var(--navy); font-weight: 700; font-size: 14px; line-height: 1.2;
  }

  .device-column { position: absolute; left: 484px; top: 0; width: 216px; height: 440px; }
  .device-icons { position: absolute; left: 18px; top: 36px; width: 180px; height: 24px; }
  .phone-photo {
    position: absolute; left: 48px; top: 120px; width: 122px; height: 170px;
    border-radius: 14px;
    background: linear-gradient(160deg, #f4ede6 0%, #d9c3b3 45%, #c9d4e4 100%);
  }
  .product-band {
    position: absolute; left: 8px; top: 300px; width: 200px; height: 32px;
    background: var(--band); color: #fff;
    font-weight: 700; font-size: 15px;
    display: flex; align-items: center; justify-content: center;
  }

  /* ---------- front side ---------- */
  .postcard-front {
    position: absolute; left: 250px; top: 520px;
    width: 700px; height: 440px;
    background: var(--bezel);
    border: 2px solid var(--bezel-edge);
    border-radius: 26px;
    box-shadow: 0 4px 14px rgba(0,0,0,.25);
  }
  .front-camera {
    position: absolute; left: 26px; top: 50%; width: 5px; height: 5px;
    margin-top: -2px; border-radius: 50%; background: #3a3f6a;
  }
  .home-button {
    position: absolute; right: 12px; top: 50%; width: 30px; height: 30px; margin-top: -15px;
    border-radius: 50%; border: 2px solid #555; background: #111;
    display: flex; align-items: center; justify-content: center;
  }
  .home-button::after {
    content: ""; width: 10px; height: 10px; border: 1.5px solid #ccc; border-radius: 2px;
  }
  .video-screen {
    position: absolute; left: 62px; top: 24px; right: 56px; bottom: 26px;
    border-radius: 18px; overflow: hidden;
    background: linear-gradient(120deg, #e9d3c2 0%, #f3efe9 35%, #dfe6ee 60%, #8fa3c8 100%);
  }
  .patient-inset {
    position: absolute; right: 28px; top: 22px; width: 146px; height: 206px;
    background: #fff; padding: 6px;
  }
  .patient-inset .photo {
    width: 100%; height: 100%;
    background: linear-gradient(170deg, #c9a98a 0%, #8a5a3c 45%, #d8d24a 100%);
  }
  .end-call {
    position: absolute; left: 236px; bottom: 12px;
    width: 122px; height: 36px; border-radius: 10px;
    background: var(--pill); color: #fff;
    display: flex; align-items: center; justify-content: center; gap: 12px;
    font-size: 18px; font-weight: 600;
  }
</style>
</head>
<body>

<section class="postcard-back" aria-label="Postcard back">
  <svg class="node-map" viewBox="0 0 200 240" aria-label="Care network diagram">
    <g stroke="#555" stroke-width="1.5">
      <line x1="100" y1="125" x2="88" y2="40"/>
      <line x1="100" y1="125" x2="160" y2="60"/>
      <line x1="100" y1="125" x2="178" y2="150"/>
      <line x1="100" y1="125" x2="120" y2="200"/>
      <line x1="100" y1="125" x2="42" y2="180"/>
      <line x1="100" y1="125" x2="24" y2="100"/>
    </g>
    <g fill="var(--green)" stroke="var(--green-edge)" stroke-width="2">
      <circle cx="88" cy="40" r="22"/>
      <circle cx="160" cy="60" r="22"/>
      <circle cx="178" cy="150" r="22"/>
      <circle cx="120" cy="200" r="22"/>
      <circle cx="42" cy="180" r="22"/>
      <circle cx="24" cy="100" r="22"/>
    </g>
    <circle cx="100" cy="125" r="44" fill="var(--navy-deep)" stroke="#fff" stroke-width="2"/>
    <text x="100" y="120" font-size="13" text-anchor="middle">Veltrona</text>
    <text x="100" y="136" font-size="13" text-anchor="middle">Patiente</text>
    <g font-size="6" text-anchor="middle">
      <text x="88" y="38">Physicians &amp;</text>
      <text x="88" y="46">Clinicians</text>
      <text x="160" y="63" font-size="8">Intake</text>
      <text x="178" y="153">Pharmacy</text>
      <text x="120" y="203">Nursing</text>
      <text x="42" y="183">Clinical Trials</text>
      <text x="24" y="103">Community</text>
    </g>
  </svg>

  <div class="column-rule left"></div>

  <div class="copy-column">
    <h2 class="section-title"><span>Introducing CareLoom:</span><span>Innovation in Patient-Centered Care</span></h2>
    <p class="intro-text">The new technology-driven solution from Veltrona, called CareLoom, allows physicians and nurse to easily capture information about the treatments of rare and complex diseases and patients responses to them ultimately improving patient outcomes and reducing costs. CareLoom gives physicians the ability to optimize dosing, determine the best therapy strategies and identify natural and non-responders.</p>
    <h2 class="section-title feature-title"><span>Introducing CareLoom:</span><span>Innovation in Patient-Centered Care</span></h2>
    <ul class="feature-list">
      <li>Infusion nurse data collection.</li>
      <li>Zolvo data entry tool.</li>
      <li>Validated outcomes assessments.</li>
      <li>Web-based physician data access.</li>
      <li>Dose vs outcomes analysis and reporting.</li>
    </ul>
    <span class="wordmark">CareLoom</span>
  </div>

  <div class="column-rule right"></div>

  <div class="device-column">
    <svg class="device-icons" viewBox="0 0 180 24" aria-label="Phone, tablet, laptop and desktop icons" fill="none" stroke="#222" stroke-width="1.6">
      <rect x="6" y="3" width="11" height="18" rx="2"/>
      <rect x="50" y="4" width="20" height="15" rx="2"/>
      <rect x="100" y="4" width="20" height="13" rx="1"/>
      <line x1="96" y1="19" x2="124" y2="19"/>
      <rect x="146" y="4" width="18" height="13" rx="1"/>
      <line x1="152" y1="20" x2="160" y2="20"/>
      <rect x="166" y="5" width="8" height="15" rx="1.5"/>
    </svg>
    <div class="phone-photo" role="img" aria-label="Hand holding a smartphone showing a video call with a doctor"></div>
    <div class="product-band">CareLoom</div>
  </div>
</section>

<section class="postcard-front" aria-label="Postcard front">
  <span class="front-camera"></span>
  <div class="video-screen" role="img" aria-label="Smiling doctor in a white coat with stethoscope on a video call, staff blurred in a bright hospital corridor behind him">
    <div class="patient-inset">
      <div class="photo" role="img" aria-label="Patient with curly hair in a yellow sweater on the video call"></div>
    </div>
    <div class="end-call">
      <svg width="26" height="12" viewBox="0 0 26 12" aria-hidden="true">
        <path d="M2 9 C2 2 24 2 24 9 L19 10 L18 6 C14 5 12 5 8 6 L7 10 Z" fill="#fff"/>
      </svg>
      <span>End</span>
    </div>
  </div>
  <span class="home-button"></span>
</section>

</body>
</html>
```